Business Stationery
Business card, letter head and compliment slip
Professional
Jake Hollins
Managing Director
Four Larkmead Row
Birmingham
B7 4QN
jake@corvastel.org.uk
corvastel.org.uk
Corvastel is an appointed representative of Pelvarin Ltd which is authorised and regulated by the Market Conduct Tribunal.

```html
<!DOCTYPE html>
<html lang="en">
<head>
<meta charset="utf-8">
<title>Corvastel Business Stationery</title>
<link href="https://fonts.googleapis.com/css2?family=Arimo:wght@400;700&display=swap" rel="stylesheet">
<style>
:root{
  --red:#d7141c;
  --red-dark:#8e0a10;
  --ink:#1c1c1c;
  --muted:#555;
  --paper:#ffffff;
  --card-grey:#c9c9c9;
  --rule:#e2b9bb;
  --label:#f3dada;
}
*{box-sizing:border-box;margin:0;padding:0}
html,body{width:1200px;height:737px;overflow:hidden}
body{
  font-family:"Arimo",Arial,sans-serif;
  color:var(--ink);
  background:radial-gradient(ellipse 900px 600px at 30% 25%, #c1121b 0%, #6e070c 55%, #120000 100%);
  position:relative;
}
.sheet{position:absolute;background:var(--paper);box-shadow:0 4px 14px rgba(0,0,0,.45);overflow:hidden}
.label{position:absolute;color:var(--label);font-size:12px}
.brand{display:flex;flex-direction:column;line-height:1}
.brand-row{display:flex;align-items:center;gap:6px}
.brand-mark{width:18px;height:18px;background:var(--red)}
.brand-name{font-weight:700;color:var(--ink);letter-spacing:-.5px}
.brand-tag{font-size:8px;color:var(--ink);margin-top:3px}
.address{font-size:9px;line-height:1.35;color:var(--ink);position:absolute}
.contacts{position:absolute;font-size:8.5px;line-height:1.55;list-style:none}
.contacts li{display:flex;align-items:center;gap:5px}
.contacts svg{width:8px;height:8px;flex:none}
.web{position:absolute;color:var(--red);font-weight:700;font-size:10px}
.band{position:absolute;left:0;right:0;background:var(--red)}

/* letterhead */
.letterhead{left:463px;top:24px;width:545px;height:708px}
.letterhead .brand{position:absolute;left:40px;top:64px}
.letterhead .brand-name{font-size:34px}
.letterhead .address{left:402px;top:72px}
.letterhead .contacts{left:52px;top:604px}
.letterhead .web{right:30px;top:668px}
.letterhead .band{bottom:0;height:10px}

/* compliment slip */
.comp-slip{left:46px;top:312px;width:552px;height:276px}
.comp-slip .brand{position:absolute;left:24px;top:34px}
.comp-slip .brand-name{font-size:30px}
.comp-slip .address{left:26px;top:96px}
.comp-slip .signatory{position:absolute;left:30px;top:226px;font-size:9px;font-weight:700}
.comp-slip .greeting{position:absolute;left:205px;top:60px;color:var(--red);font-size:11px;font-weight:700;letter-spacing:.5px}
.comp-slip .lines{position:absolute;left:205px;top:96px;width:310px}
.comp-slip .lines span{display:block;height:1px;background:var(--rule);margin-bottom:19px}
.comp-slip .divider{position:absolute;left:188px;top:50px;width:1px;height:200px;background:var(--rule)}
.comp-slip .band{bottom:0;height:10px}

/* business card front */
.card-front{left:780px;top:140px;width:391px;height:368px}
.card-front .band-top{position:absolute;left:0;right:0;top:0;height:8px;background:var(--red)}
.card-front .address{left:22px;top:30px}
.card-front .person{position:absolute;left:130px;top:114px;font-size:9px;display:flex;gap:8px;align-items:center}
.card-front .person strong{font-weight:700}
.card-front .person .sep{width:1px;height:12px;background:var(--ink)}
.card-front .contacts{left:22px;top:186px}
.card-front .web{left:22px;top:302px}
.card-front .brand{position:absolute;right:24px;top:268px}
.card-front .brand-name{font-size:38px}
.card-front .band{bottom:0;height:10px}

/* business card back */
.card-back{left:780px;top:533px;width:391px;height:172px;background:var(--card-grey)}
.card-back .brand{position:absolute;left:24px;top:62px}
.card-back .brand-name{font-size:28px}
.card-back .rule{position:absolute;left:198px;top:40px;width:1px;height:92px;background:var(--muted)}
.card-back .statement{position:absolute;left:210px;top:62px;width:160px;font-size:8px;line-height:1.5;color:#333}
</style>
</head>
<body>

<span class="label" style="left:905px;top:6px">Letterhead : A4</span>
<span class="label" style="left:1098px;top:120px">Bizcard Front</span>
<span class="label" style="left:276px;top:630px">comp slips</span>
<span class="label" style="left:1102px;top:714px">Bizcard Back</span>

<section class="sheet letterhead">
  <div class="brand">
    <div class="brand-row"><span class="brand-mark"></span><span class="brand-name">corvastel</span></div>
    <span class="brand-tag">Independent financial advice for doctors</span>
  </div>
  <address class="address">Four Larkmead Row<br>Birmingham<br>B7 4QN</address>
  <ul class="contacts">
    <li><svg viewBox="0 0 8 8"><rect width="8" height="8" fill="#d7141c"/></svg>t : 0121 496 0218</li>
    <li><svg viewBox="0 0 8 8"><rect width="8" height="8" fill="#d7141c"/></svg>m : 07700 900461</li>
    <li><svg viewBox="0 0 8 8"><rect width="8" height="8" fill="#d7141c"/></svg>f : 0121 496 0733</li>
    <li><svg viewBox="0 0 8 8"><rect width="8" height="8" fill="#d7141c"/></svg>e : jake@corvastel.org.uk</li>
  </ul>
  <span class="web">corvastel.org.uk</span>
  <div class="band"></div>
</section>

<section class="sheet comp-slip">
  <div class="brand">
    <div class="brand-row"><span class="brand-mark"></span><span class="brand-name">corvastel</span></div>
    <span class="brand-tag">Independent financial advice for doctors</span>
  </div>
  <address class="address">Four Larkmead Row<br>Birmingham<br>B7 4QN</address>
  <span class="signatory">Jake Hollins</span>
  <span class="divider"></span>
  <span class="greeting">With compliments</span>
  <div class="lines"><span></span><span></span><span></span><span></span><span></span><span></span></div>
  <div class="band"></div>
</section>

<section class="sheet card-front">
  <div class="band-top"></div>
  <address class="address">Four Larkmead Row<br>Birmingham<br>B7 4QN</address>
  <div class="person"><strong>Jake Hollins</strong><span class="sep"></span><span>Managing Director</span></div>
  <ul class="contacts">
    <li><svg viewBox="0 0 8 8"><rect width="8" height="8" fill="#d7141c"/></svg>t : 0121 496 0218</li>
    <li><svg viewBox="0 0 8 8"><rect width="8" height="8" fill="#d7141c"/></svg>m : 07700 900461</li>
    <li><svg viewBox="0 0 8 8"><rect width="8" height="8" fill="#d7141c"/></svg>f : 0121 496 0733</li>
    <li><svg viewBox="0 0 8 8"><rect width="8" height="8" fill="#d7141c"/></svg>e : jake@corvastel.org.uk</li>
  </ul>
  <span class="web">corvastel.org.uk</span>
  <div class="brand">
    <div class="brand-row"><span class="brand-mark"></span><span class="brand-name">corvastel</span></div>
    <span class="brand-tag">Independent financial advice for doctors</span>
  </div>
  <div class="band"></div>
</section>

<section class="sheet card-back">
  <div class="brand">
    <div class="brand-row"><span class="brand-mark"></span><span class="brand-name">corvastel</span></div>
    <span class="brand-tag">Independent financial advice for doctors</span>
  </div>
  <span class="rule"></span>
  <p class="statement">Corvastel is an appointed representative of Pelvarin Ltd which is authorised and regulated by the Market Conduct Tribunal.</p>
</section>

</body>
</html>
```